Email Banner - TamberFold.com

I need an email banner created for my website: Tamberfold.com.
The logos are attatched here and an example of an email banner we have used in the past is also attatched. Please keep the tagline: "Essential Whitepapers for Business Professionals" - The logos are in the marvotta zip folder.

Logo Text

Tamberfold

```html
<!DOCTYPE html>
<html lang="en">
<head>
<meta charset="utf-8">
<title>Tamberfold Email Banner</title>
<link rel="stylesheet" href="https://fonts.googleapis.com/css2?family=Figtree:wght@400;500;600;700&display=swap">
<style>
  :root {
    --page-bg: #eff1f5;
    --navy: #252f80;
    --blue: #3a6cff;
    --blue-light: #8aa8ff;
    --white: #ffffff;
    --bar-tint: rgba(255, 255, 255, 0.28);
    --bar-tint-2: rgba(255, 255, 255, 0.38);
  }
  * { box-sizing: border-box; margin: 0; padding: 0; }
  html, body {
    width: 1200px;
    height: 1200px;
    overflow: hidden;
    background: var(--page-bg);
    font-family: "Figtree", sans-serif;
  }
  .banner {
    position: absolute;
    left: 118px;
    top: 524px;
    width: 964px;
    height: 151px;
    background: var(--navy);
    overflow: hidden;
  }
  .banner__wave {
    position: absolute;
    inset: 0;
  }
  .brand {
    position: absolute;
    left: 0;
    width: 342px;
    top: 0;
    height: 151px;
    display: flex;
    align-items: center;
    justify-content: center;
  }
  .brand__name {
    color: var(--white);
    font-weight: 600;
    font-size: 46px;
    letter-spacing: -0.5px;
  }
  .tagline {
    position: absolute;
    left: 421px;
    top: 52px;
    color: var(--white);
    font-size: 25px;
    line-height: 32px;
    font-weight: 400;
  }
  .tagline strong { font-weight: 600; }
  .cta {
    position: absolute;
    left: 799px;
    top: 8px;
    width: 175px;
    height: 37px;
    border-radius: 5px;
    background: var(--blue);
    color: var(--white);
    font-weight: 700;
    font-size: 19px;
    line-height: 37px;
    padding-left: 25px;
    letter-spacing: 0.2px;
  }
  .cta-bar {
    position: absolute;
    left: 799px;
    width: 175px;
    height: 38px;
    border-radius: 5px;
  }
  .cta-bar--one { top: 57px; background: var(--bar-tint); }
  .cta-bar--two { top: 106px; background: var(--bar-tint-2); }
</style>
</head>
<body>
  <div class="banner">
    <svg class="banner__wave" width="964" height="151" viewBox="0 0 964 151" aria-hidden="true">
      <defs>
        <linearGradient id="waveFill" x1="0" y1="0" x2="1" y2="0">
          <stop offset="0" stop-color="#3a6cff"/>
          <stop offset="0.45" stop-color="#4f7dff"/>
          <stop offset="1" stop-color="#8aa8ff"/>
        </linearGradient>
      </defs>
      <path d="M358 151 C358 70 410 0 500 0 L964 0 L964 151 Z" fill="url(#waveFill)"/>
    </svg>

    <div class="brand">
      <span class="brand__name">Tamberfold</span>
    </div>

    <p class="tagline">Essential Whitepapers<br>for <strong>Business Professionals</strong></p>

    <div class="cta">CLICK HERE</div>
    <div class="cta-bar cta-bar--one"></div>
    <div class="cta-bar cta-bar--two"></div>
  </div>
</body>
</html>
```